Nutritional & Gastrointestinal Health Consulting Service-Website design

We need a website design for a new health consulting service called "Bright Meadow" based in Perth, Australia.

We will be providing consulting services in the areas of:
1) Nutrition and Diet
2) Gastrointestinal Health (which means stomach & digestive system related health)

These consulting services will be provided by an Accredited Dietitian and a Paediatric Gastroenterologist.

We are open to creative ideas in terms of design, layout, fonts and colours. We also would love to see images of nature in the backdrop with families (adults with kids) having a good time, fresh fruits and vegetables displayed in a farmer's market or supermarket. 2 or 3 images should be sufficient. We would also definitely want our logo somewhere in the main page of website. The logo file is also attached. Please have a look at a website's design that we really liked. We would love to see designs inspired by that style. The website details are in the in the "nice to have priorities" section of this project brief.

We also would be looking at website designers with software coding skills so that if we like the design we can go ahead with the next step of coding.

The website design should communicate the purpose of the website and at the same time be simple, elegant and unique/eye-catching.

We look forward to receiving creative ideas for our website from you all. Good luck!

More details have been added to our project- for example: Logo, fonts style, must haves etc etc. Please view the updated project brief. Looking forward to receiving your fantastic ideas for our website. Thanking you

Hi, I have updated the colour preference. Will add the content preferences tomorrow. thanks

Hello all, I have now added a LOT more content to what we want in our website. It is very much in detail, so please carefully have a read through the entire project brief. If you have any questions write back to me and I will try to respond as quickly as I can. Last few days were busy so couldn't respond quickly to all of you who had send me designs/queries/questions. Thank you for your patience. I look forward to receiving fantastic designs from you all. Good Luck :-)

Target Market(s)

Adults based in western speaking countries aged 18 to 60 years

Industry/Entity Type

Software

Font styles to use
Sans Serif
Script

Colors
faa54b
acd036

Requirements
Must have
• The website must have the MAIN logo file attached. I have attached 3 files: 1) MAIN logo; 2) supplementary logo A ; 3) supplementary logo B

I have selected 2 colours from the colour scheme (see below)-(as the colour of our logo is that).
However we would also like to see LIGHT CHOCOLATE BROWN or CHOCOLATE BROWN colour used as the background colour of the website
Preferred WEBSITE CONTENT:
1) HOME PAGE:
Content required=
--Company Logo
--Dr Rowan Pellfry
Paediatric Gastroenterologist & Hepatologist
-Lena Pellfry.
Dietitian & Nutritionist
--Website Menu (either listed horizontally or vertically):
Once clicked on each name:

Under each of the Website Menu items we want the following Headings to be added

2) ABOUT US page:
Sub-heading under this: Qualification, Skills, Special Interest

3) SERVICES
ROWAN'S PAGE: Individual Consultation, Endoscopy procedures
Individual Consultation, Group Based Services, Food Diary, Food & Symptom Diary

4) FEES & REBATE: Content as below:
Please Note: Payment of full fees is required at the time of consultation and procedures. 48 hours notice is required for cancellation of appointments/non-attendance. Failure to provide this may result in a fee being incurred. Please call reception to find out the amount of fee charged for cancellation of appointments/non-attendance.
headings are:
Paediatric Gastroenterology:
Rowan's pge
Individual Consultation - Initial (upto 30 mins):
Review Consultation (upto 15 mins):
Endoscopy procedures - No Gap fees charged. Fees will be billed directly to Vitacover. If any queries, please contact reception.

lena's pge
sub heading:
Individual Consultation - Initial (upto 45 mins):
Individual Consultation - Review (upto 30 mins):

Concession-Individual Consultation -Initial (upto 45 mins):
Concession-Individual Consultation - Review (upto 30 mins):
Please Note: Concession applies for health care card holders & pensioners

Group Based Services: Pricing subject to the type of service provided. Please contact us for an obligation free quote.
Education Topics Include:
- Paediatric Nutrition (Introducing Solids, Fussy Eating, Healthy Eating)
- Pregnancy Nutrition, Gestational Diabetes, Breastfeeding/Lactation Nutrition
- Healthy Eating, Supermarket Shopping Tips, Nutrition Label Reading Tips, Healthier
sub heading under nutrition & diet:
-Vitacover:
--A rebate of $52.95 is available from Vitacover if an EPC ( Enhanced Primary Care)/Chronic Disease Management (CDM) plan is issued by your GP.
--All mandatory paperwork needs to be available at the time of making your appointment for your eligibility.
-Private Health Fund:
--Most private health funds provide rebate on dietetic appointments. However the rebate amount depends on your level of cover. Thus, please contact your health fund to determine your entitled rebate.
-KRB: Approved provider for KRB services

6) FOR DOCTORS: Bright Meadow Paediatric Gastroenterologist Referral Form
Bright Meadow Dietitian Referral form
7) LOCATIONS & CONTACT

Paediatric Gastroenterology & Hepatology Service
Suite 46
Fairholt Grange Larchmont Medical Centre
17 Oswin Talbot Pde,
MURDOCH, WA 6150
P: (08) 9462 3051
F: (08) 9462 7309

Nutrition & Diet Service
Suite 46
17 Oswin Talbot Pde,
MURDOCH, WA 6150
P: (08) 9462 3051
F: (08) 9462 7309

Quill Medical Centre
52-54 Tarrago Parkway,
MANDURAH, WA 6210
P: (08) 9728 4402
F: (08) 96274518
www.qmcbaylow.com.au

This page should have a webform that has following titles:
-Your Name
-Your Email
-Your Phone
-Message

8) NEWS & BLOG
Nice to have
• We liked the design style of the websites below:
https://www.wellvorn.example/

http://tummyplex.example/

But feel free to use your creativity too
Should not have
• Please do not use any body building or muscle building images

```html
<!DOCTYPE html>
<html lang="en">
<head>
<meta charset="utf-8">
<title>Bright Meadow – Fees &amp; Rebate</title>
<link rel="stylesheet" href="https://fonts.googleapis.com/css2?family=Arimo:wght@400;700&display=swap">
<style>
  :root {
    --choc: #5b3519;
    --choc-light: #7a4e2c;
    --frame-fill: #b9a796;
    --panel-fill: #d8cec6;
    --edge: #f4f2f0;
    --edge-shadow: #8f8a86;
    --rule: #a9a6a4;
    --ink: #111111;
  }
  * { box-sizing: border-box; margin: 0; padding: 0; }
  html, body {
    width: 1200px; height: 900px; overflow: hidden;
    font-family: "Arimo", Arial, sans-serif; color: var(--ink);
  }
  .backdrop {
    position: absolute; inset: 0;
    background: radial-gradient(circle at 50% 40%, var(--choc-light), var(--choc) 70%);
  }
  .site-frame {
    position: absolute; left: 35px; top: -20px; width: 1130px; height: 882px;
    background: var(--frame-fill);
    border: 3px solid var(--edge);
    border-top: none;
    border-radius: 0 0 14px 14px;
    box-shadow: 0 2px 0 var(--edge-shadow);
  }
  .content-panel {
    position: absolute; left: 296px; top: -20px; width: 607px; height: 820px;
    background: var(--panel-fill);
    border: 2px solid var(--edge);
    border-top: none;
    border-radius: 0 0 8px 8px;
    box-shadow: 0 1px 0 var(--edge-shadow);
  }
  .content { position: absolute; left: 322px; width: 556px; }
  .content > * { position: absolute; left: 0; width: 556px; }
  p { font-size: 13px; line-height: 15px; }
  .note { font-weight: 700; }
  .section-title { font-size: 17px; font-weight: 700; line-height: 20px; }
  .rate-title { font-size: 15px; font-weight: 700; text-decoration: underline; line-height: 18px; }
  .rebate-title { font-size: 17px; font-weight: 700; text-decoration: underline; line-height: 20px; }
  .panel-rule {
    position: absolute; left: 322px; top: 774px; width: 556px; height: 3px;
    background: var(--rule); border-bottom: 1px solid var(--edge);
  }
  .site-footer {
    position: absolute; left: 0; width: 1200px; top: 824px;
    text-align: center; font-size: 13px; font-weight: 700; line-height: 15px;
  }
  .site-footer a { color: var(--ink); }
</style>
</head>
<body>
  <div class="backdrop" role="img" aria-label="Chocolate brown background with a pattern of hand-drawn fruit, vegetables and food"></div>
  <div class="site-frame"></div>
  <div class="content-panel"></div>

  <main class="content">
    <p style="top:-7px">massa, nec interdum augue eros vel neque.</p>
    <h2 class="section-title" style="top:20px">Concession - Individual Consultation</h2>
    <p class="note" style="top:54px">Please Note: Concession applies for health care card holders &amp; pensioners.</p>

    <h3 class="rate-title" style="top:83px">Initial (upto 45 mins)</h3>
    <p style="top:116px">Vivamus vitae dolor a mauris sollicitudin posuere quis a lectus. Nunc fringilla quam non massa iaculis, vel imperdiet dui gravida.</p>

    <h3 class="rate-title" style="top:159px">Review (upto 30 mins)</h3>
    <p style="top:192px">Fusce nec justo rutrum, egestas sapien quis, congue velit. Duis vel nisl nibh. Mauris sed nisl et massa sagittis blandit. Nam augue neque, sollicitudin et arcu sed, ultrices sagittis nulla.</p>

    <h2 class="rebate-title" style="top:235px">Vitacover:</h2>
    <p style="top:269px">- A rebate of $52.95 is available from Vitacover if an EPC ( Enhanced Primary Care)/Chronic Disease Management (CDM) plan is issued by your GP.</p>
    <p style="top:314px">- All mandatory paperwork needs to be available at the time of making your appointment for your eligibility.</p>

    <h2 class="rebate-title" style="top:357px">Private Health Fund:</h2>
    <p style="top:391px">- Most private health funds provide rebate on dietetic appointments. However the rebate amount depends on your level of cover. Thus, please contact your health fund to determine your entitled rebate.</p>

    <h2 class="rebate-title" style="top:449px">KRB</h2>
    <p style="top:483px">- Approved provider for KRB services</p>

    <h2 class="section-title" style="top:511px">Group Based Services</h2>
    <p class="note" style="top:545px">Pricing subject to the type of service provided. Please contact us for an obligation free quote.</p>
    <p class="note" style="top:590px">Education Topics Include:</p>
    <p style="top:621px">- Paediatric Nutrition (Introducing Solids, Fussy Eating, Healthy Eating)</p>
    <p style="top:651px">- Pregnancy Nutrition, Gestational Diabetes, Breastfeeding/Lactation Nutrition</p>
    <p style="top:681px">- Healthy Eating, Supermarket Shopping Tips, Nutrition Label Reading Tips, Healthier Cooking Ideas</p>
    <p style="top:727px">- Weight Management, Diabetes Management, Heart Health and a few more</p>
  </main>

  <div class="panel-rule"></div>

  <footer class="site-footer">
    <a href="#">Bright Meadow</a> © Copyright 2014
  </footer>
</body>
</html>
```